Home Security Company Business Card

Looking for a eye catching business card that is non traditional and stands out but yet still looks professional. It should include all the pertinent information such as name, title, address, telephone, e-mail, website address should definitely stand out and then finally the logo.

Target Market(s)

Residential and Commercial accounts mostly upscale accounts

Industry/Entity Type

Security

Contact Information for Business Card

Name
Title
Address
Office #
Cell #
E-mail
Website

Font styles to use
Serif
Sans Serif

Requirements
Must have
• Logo, two sided color configuration
Nice to have
• You decide
Should not have
• There really aren't any.

```html
<!DOCTYPE html>
<html lang="en">
<head>
<meta charset="utf-8">
<title>Wardline Security Systems – Business Card</title>
<link rel="stylesheet" href="https://fonts.googleapis.com/css2?family=Quicksand:wght@400;500;700&display=swap">
<style>
  :root {
    --backdrop: #eceef0;
    --card-white: #f7f7f7;
    --brand-red: #84201c;
    --brand-gold: #dcaa3f;
    --brand-grey: #bcbdbf;
    --text-light: #ffffff;
    --text-soft: #f3e3e1;
  }
  * { box-sizing: border-box; margin: 0; padding: 0; }
  html, body {
    width: 1200px; height: 800px; overflow: hidden;
    background: var(--backdrop);
    font-family: "Quicksand", Arial, sans-serif;
  }
  .canvas {
    position: relative; width: 1200px; height: 800px;
  }
  .card {
    position: absolute; top: 102px;
    width: 340px; height: 595px;
    overflow: hidden;
    box-shadow: 0 14px 30px rgba(0,0,0,.12), 0 2px 6px rgba(0,0,0,.08);
  }
  .card--back { left: 210px; }
  .card--front { left: 650px; }
  .card__shapes { position: absolute; inset: 0; width: 100%; height: 100%; display: block; }

  .wordmark {
    position: absolute;
    display: flex; align-items: center; gap: 12px;
    color: var(--brand-red);
    font-weight: 700; font-size: 19px; line-height: 1.15;
    letter-spacing: .06em; text-transform: uppercase;
  }
  .wordmark__dot {
    width: 44px; height: 44px; border-radius: 50%;
    background: var(--brand-gold); flex: none;
  }
  .card--back .wordmark { left: 60px; top: 118px; }
  .card--front .wordmark { left: 66px; top: 94px; }

  .identity {
    position: absolute; left: 128px; top: 279px;
    display: flex; align-items: flex-start; gap: 10px;
    color: var(--text-light);
    transform: rotate(8.4deg); transform-origin: left top;
  }
  .identity__icon { width: 20px; height: 22px; flex: none; margin-top: 2px; }
  .identity__name { font-size: 19px; font-weight: 400; letter-spacing: .04em; line-height: 1; }
  .identity__name strong { font-weight: 700; }
  .identity__title { font-size: 10px; letter-spacing: .12em; margin-top: 3px; }

  .contacts {
    position: absolute; left: 34px; top: 390px;
    list-style: none; color: var(--text-soft);
    font-size: 13px; line-height: 1.35;
  }
  .contacts li { display: flex; gap: 14px; margin-bottom: 16px; }
  .contacts svg { width: 16px; height: 16px; flex: none; margin-top: 1px; }
</style>
</head>
<body>
<main class="canvas">

  <!-- Reverse side -->
  <section class="card card--back" aria-label="Card reverse">
    <svg class="card__shapes" viewBox="0 0 340 595" aria-hidden="true">
      <rect width="340" height="595" fill="var(--brand-red)"/>
      <polygon points="0,0 340,0 340,262 110,300 0,248" fill="var(--card-white)"/>
      <polygon points="236,0 340,0 340,96" fill="var(--brand-gold)"/>
    </svg>
    <div class="wordmark">
      <span class="wordmark__dot"></span>
      <span>Wardline<br>Security Systems Inc.</span>
    </div>
  </section>

  <!-- Front side -->
  <section class="card card--front" aria-label="Card front">
    <svg class="card__shapes" viewBox="0 0 340 595" aria-hidden="true">
      <rect width="340" height="595" fill="var(--brand-grey)"/>
      <polygon points="26,0 340,0 340,276 26,226" fill="var(--card-white)"/>
      <polygon points="0,240 340,290 340,360 0,300" fill="var(--brand-gold)"/>
      <polygon points="0,300 340,360 340,556 0,556" fill="var(--brand-red)"/>
    </svg>

    <div class="wordmark">
      <span class="wordmark__dot"></span>
      <span>Wardline<br>Security Systems Inc.</span>
    </div>

    <div class="identity">
      <svg class="identity__icon" viewBox="0 0 20 22" aria-hidden="true">
        <circle cx="10" cy="6" r="5" fill="var(--text-light)"/>
        <path d="M0 22 C0 14 20 14 20 22 Z" fill="var(--text-light)"/>
      </svg>
      <div>
        <p class="identity__name">DANIEL <strong>REYES</strong></p>
        <p class="identity__title">OWNER</p>
      </div>
    </div>

    <ul class="contacts">
      <li>
        <svg viewBox="0 0 16 16" aria-hidden="true"><path d="M4 1 L6.5 4.5 L5 6.5 C6 8.5 7.5 10 9.5 11 L11.5 9.5 L15 12 L13 15 C7 14.5 1.5 9 1 3 Z" fill="none" stroke="var(--text-light)" stroke-width="1.4" stroke-linejoin="round"/></svg>
        <span>Office: 555 014 2290<br>Cell: 555 014 2291</span>
      </li>
      <li>
        <svg viewBox="0 0 16 16" aria-hidden="true"><g fill="none" stroke="var(--text-light)" stroke-width="1.2"><circle cx="8" cy="8" r="7"/><ellipse cx="8" cy="8" rx="3" ry="7"/><path d="M1 8 H15 M2.5 4.5 H13.5 M2.5 11.5 H13.5"/></g></svg>
        <span>www.wardlinesecurity.com<br>daniel@wardlinesecurity.com</span>
      </li>
      <li>
        <svg viewBox="0 0 16 16" aria-hidden="true"><path d="M8 15 C4 10 3 8 3 6 A5 5 0 0 1 13 6 C13 8 12 10 8 15 Z" fill="var(--text-light)"/><circle cx="8" cy="6" r="1.8" fill="var(--brand-red)"/></svg>
        <span>Address Line 1<br>Address Line 2</span>
      </li>
    </ul>
  </section>

</main>
</body>
</html>
```